8X8 Realtor Training Expo Flyer

BRAVO SUMMIT REALTY & HALCYON REALTY VENTURES
INVITE ALL TO OUR
LIVE REALTOR TRAINING EXPO

WITH TRAINER / SPEAKER MR. GORDON ALAPATI
SATURDAY AUGUST 13th
9 AM - 1 PM
AT THE MARWICK LODGE
4817 HOLLOWAY CREEK DRIVE
GREENBELT, MD 20770

RSVP PREFERRED BY EMAILING FRONTDESK@BRAVOSUMMITREALTY.COM

```html
<!DOCTYPE html>
<html lang="en">
<head>
<meta charset="utf-8">
<title>Live Realtor Training Expo Flyer</title>
<link href="https://fonts.googleapis.com/css2?family=Anton&family=Poppins:wght@400;600;700&display=swap" rel="stylesheet">
<style>
  :root {
    --teal: #12909a;
    --teal-dark: #4b8690;
    --teal-mid: #80b0b9;
    --teal-light: #a8c7ce;
    --sky: #f0f0ec;
    --ink: #2b2b2b;
    --paper: #ffffff;
    --stage: #e4e6e5;
  }
  * { box-sizing: border-box; margin: 0; padding: 0; }
  html, body { width: 1156px; height: 1200px; overflow: hidden; background: var(--stage); }
  body { position: relative; font-family: "Poppins", sans-serif; }

  .flyer {
    position: absolute; left: 0; top: 22px;
    width: 1348px; height: 1348px;
    background: var(--paper);
    transform: scale(0.857567); transform-origin: 0 0;
    overflow: hidden;
  }
  .skyline {
    position: absolute; left: 51px; top: 84px; width: 943px; height: 520px;
    background: linear-gradient(180deg, var(--sky) 0%, var(--sky) 20%, var(--teal-light) 55%, var(--teal-mid) 80%, var(--teal-dark) 100%);
  }
  .headline { position: absolute; left: 51px; top: 606px; width: 943px; height: 500px; overflow: visible; }
  .headline text { font-family: "Anton", sans-serif; }

  .brands {
    position: absolute; left: 1038px; top: 60px; width: 280px;
    text-align: center; color: var(--teal);
    font-weight: 700; font-size: 30px; line-height: 1.15;
  }
  .brand { height: 170px; display: flex; align-items: center; justify-content: center; }
  .amp {
    width: 44px; height: 44px; margin: 6px auto; border-radius: 50%;
    background: var(--teal); color: #fff;
    font-size: 28px; font-weight: 600; line-height: 44px;
  }

  .speaker-photo {
    position: absolute; left: 1048px; top: 878px; width: 270px; height: 260px;
    background: linear-gradient(180deg, #5a5a5a, #2e2e2e);
    border-radius: 120px 120px 0 0;
  }
  .speaker-panel { position: absolute; left: 1010px; top: 1108px; width: 338px; height: 240px; }
  .speaker-text {
    position: absolute; left: 1010px; top: 1150px; width: 338px;
    text-align: center; color: #fff; font-size: 21px; line-height: 28px;
  }
  .speaker-text strong { display: block; font-weight: 700; font-size: 22px; margin-top: 4px; }

  .details { position: absolute; color: var(--ink); font-weight: 700; }
  .when { left: 70px; top: 1120px; font-size: 26px; }
  .when .row { display: flex; align-items: center; height: 52px; margin-bottom: 13px; }
  .when svg { width: 42px; height: 42px; margin-right: 21px; }
  .when sup { font-size: 14px; vertical-align: 12px; }
  .where { left: 502px; top: 1122px; display: flex; font-size: 27px; line-height: 36px; }
  .where svg { width: 46px; height: 46px; margin: 8px 28px 0 0; }

  .rsvp {
    position: absolute; left: 51px; top: 1273px; width: 944px; height: 49px;
    background: var(--teal); color: #fff;
    font-size: 26px; line-height: 49px; padding-left: 20px; white-space: nowrap;
  }
  .rsvp strong { font-weight: 700; }
</style>
</head>
<body>
<div class="flyer">
  <div class="skyline" role="img" aria-label="Illustrated city skyline of teal skyscrapers"></div>

  <svg class="headline" viewBox="0 0 943 500" aria-label="Invite all to our Live Realtor Training Expo">
    <text x="0" y="137" font-size="156" fill="var(--teal-light)" textLength="943" lengthAdjust="spacingAndGlyphs">INVITE ALL TO OUR</text>
    <text x="0" y="327" font-size="211" fill="var(--teal-mid)" textLength="943" lengthAdjust="spacingAndGlyphs">LIVE REALTOR</text>
    <text x="0" y="497" font-size="185" fill="var(--teal-dark)" textLength="943" lengthAdjust="spacingAndGlyphs">TRAINING EXPO</text>
  </svg>

  <div class="brands">
    <div class="brand">BRAVO SUMMIT<br>REALTY GROUP</div>
    <div class="amp">&amp;</div>
    <div class="brand">HALCYON REALTY<br>VENTURES</div>
  </div>

  <div class="speaker-photo" role="img" aria-label="Silhouette portrait of the trainer in a suit"></div>
  <svg class="speaker-panel" viewBox="0 0 338 240" aria-hidden="true">
    <path d="M0 8 Q170 28 338 0 L338 240 L0 240 Z" fill="var(--teal)"/>
  </svg>
  <div class="speaker-text">WITH<br>TRAINER / SPEAKER<strong>MR. GORDON ALAPATI</strong></div>

  <div class="details when">
    <div class="row">
      <svg viewBox="0 0 42 42" aria-hidden="true">
        <rect x="2" y="6" width="38" height="34" rx="4" fill="var(--teal)"/>
        <rect x="9" y="1" width="5" height="10" rx="2" fill="var(--teal)"/>
        <rect x="28" y="1" width="5" height="10" rx="2" fill="var(--teal)"/>
        <g fill="#fff">
          <rect x="8" y="18" width="6" height="5"/><rect x="18" y="18" width="6" height="5"/><rect x="28" y="18" width="6" height="5"/>
          <rect x="8" y="28" width="6" height="5"/><rect x="18" y="28" width="6" height="5"/><rect x="28" y="28" width="6" height="5"/>
        </g>
      </svg>
      <span>SATURDAY AUGUST 13<sup>th</sup></span>
    </div>
    <div class="row">
      <svg viewBox="0 0 42 42" aria-hidden="true">
        <circle cx="21" cy="21" r="20" fill="var(--teal)"/>
        <path d="M20 10 V23 L29 29" stroke="#fff" stroke-width="4" fill="none" stroke-linecap="round"/>
      </svg>
      <span>9 AM - 1 PM</span>
    </div>
  </div>

  <div class="details where">
    <svg viewBox="0 0 46 46" aria-hidden="true">
      <path d="M2 20 L44 4 L28 44 L24 24 Z" fill="var(--teal)"/>
    </svg>
    <div>At The Marwick Lodge<br>4817 Holloway Creek Drive<br>Greenbelt, MD 20770</div>
  </div>

  <div class="rsvp">RSVP Preferred by emailing <strong>frontdesk@bravosummitrealty.com</strong></div>
</div>
</body>
</html>
```